Mobile Pet Care Clinic in San Francisco Flyer

- One-page, black & white, flyer to announce our monthly Pet Care clinics.

- Included, we need a cat image and a dog image - perferably a happy-faced Pitbull type dog but not mean looking.

- We need a blank box that we can drop the date into the flyer as the clinics are announced.

- Large Warm Nose Wagon logo at the top (we've up-loaded 2 to choose from)
- Maple Harbor logo at the bottom

-Below is the copy we need included:

ANIMAL CARE CLINIC
The WNW Mobile Pet Care Team will be On-Site to Provide FREE:
- Veterinary Wellness Checks
- Vaccinations
- Microchipping
- Spay/Neuter Vouchers
- Dog Training & Management Help
- Leashes, Collars & Harnesses
- Jackets During the Winter Months
- Dog & Cat Food
- Answers to Husbandry Questions
- Toys!!!

PLEASE JOIN US!

Target Market(s)

Pet Owners

Industry/Entity Type

Pet Care

Font styles to use
Serif
Sans Serif

Requirements
Must have
• see above

```html
<!DOCTYPE html>
<html lang="en">
<head>
<meta charset="utf-8">
<title>Warm Nose Wagon – Animal Care Clinic Flyer</title>
<link rel="stylesheet" href="https://fonts.googleapis.com/css2?family=Arimo:wght@400;700&family=Nunito:wght@900&family=Archivo+Black&display=swap">
<style>
  :root {
    --page-bg: #ffffff;
    --paper: #f7f7f7;
    --banner: #7b7b7b;
    --banner-line: #ececec;
    --ink: #1e1e1e;
    --brand-grey: #5a5a5a;
    --white: #ffffff;
    --cat-light: #d9d9d9;
    --cat-dark: #8e8e8e;
    --dog-light: #5a5a5a;
    --dog-dark: #141414;
  }
  html, body {
    margin: 0;
    width: 1200px;
    height: 1200px;
    overflow: hidden;
    background: var(--page-bg);
  }
  .flyer {
    position: absolute;
    left: 212px;
    top: 58px;
    width: 968px;
    height: 1358px;
    transform: scale(0.8);
    transform-origin: top left;
    background: var(--paper);
    font-family: "Arimo", Arial, sans-serif;
    color: var(--ink);
  }
  .flyer-texture {
    position: absolute;
    inset: 0;
    background: radial-gradient(circle at 50% 40%, #fbfbfb 0%, #f1f1f1 100%);
  }
  .brand {
    position: absolute;
    left: 0;
    right: 0;
    top: 68px;
    display: flex;
    justify-content: center;
    align-items: center;
    gap: 22px;
  }
  .brand-dot {
    width: 64px;
    height: 64px;
    border-radius: 50%;
    background: var(--brand-grey);
  }
  .brand-name {
    font-weight: 700;
    font-size: 60px;
    color: var(--brand-grey);
    letter-spacing: -0.5px;
  }
  .banner {
    position: absolute;
    left: 70px;
    top: 281px;
    width: 828px;
    height: 397px;
    background: var(--banner);
  }
  .banner-frame {
    position: absolute;
    left: 22px;
    top: 27px;
    right: 22px;
    bottom: 28px;
    border: 2px solid var(--banner-line);
  }
  .title {
    position: absolute;
    z-index: 2;
    left: 112px;
    top: 78px;
    margin: 0;
    font-family: "Nunito", "Arial Rounded MT Bold", sans-serif;
    font-weight: 900;
    color: var(--white);
    line-height: 1;
  }
  .title-main {
    display: block;
    font-size: 142px;
    letter-spacing: 1px;
  }
  .title-sub {
    display: block;
    font-size: 88px;
    margin-top: 14px;
    letter-spacing: 0.5px;
  }
  .photo-cat {
    position: absolute;
    left: 115px;
    top: 198px;
    width: 280px;
    height: 155px;
    background: linear-gradient(160deg, var(--cat-light), var(--cat-dark));
    border-radius: 4px;
  }
  .photo-dog {
    position: absolute;
    z-index: 1;
    left: 792px;
    top: 488px;
    width: 128px;
    height: 300px;
    background: linear-gradient(180deg, var(--dog-light), var(--dog-dark));
    border-radius: 4px;
  }
  .intro {
    position: absolute;
    left: 70px;
    top: 790px;
    margin: 0;
    font-weight: 700;
    font-size: 21px;
  }
  .services {
    position: absolute;
    top: 845px;
    margin: 0;
    padding: 0;
    list-style: none;
    font-weight: 700;
    font-size: 17px;
  }
  .services-left { left: 72px; }
  .services-right { left: 563px; top: 842px; }
  .services li {
    position: relative;
    height: 55.4px;
    padding-left: 39px;
    line-height: 26px;
  }
  .services li::before {
    content: "";
    position: absolute;
    left: 2px;
    top: 5px;
    width: 16px;
    height: 16px;
    border-radius: 50%;
    background: var(--ink);
  }
  .join {
    position: absolute;
    left: 0;
    right: 0;
    top: 1118px;
    margin: 0;
    text-align: center;
    font-family: "Archivo Black", "Arial Black", sans-serif;
    font-size: 48px;
    line-height: 60px;
    letter-spacing: 0.5px;
  }
  .date-box {
    position: absolute;
    left: 42px;
    top: 1194px;
    width: 885px;
    height: 135px;
    box-sizing: border-box;
    border: 1.5px solid var(--ink);
  }
</style>
</head>
<body>
  <main class="flyer">
    <div class="flyer-texture" role="img" aria-label="Faint pattern of paw prints and bones across the page"></div>

    <header class="brand">
      <span class="brand-dot"></span>
      <span class="brand-name">WarmNoseWagon</span>
    </header>

    <section class="banner">
      <div class="banner-frame"></div>
      <h1 class="title">
        <span class="title-main">ANIMAL</span>
        <span class="title-sub">CARE CLINIC</span>
      </h1>
    </section>

    <div class="photo-cat" role="img" aria-label="Photo of a tabby cat lying on top of the banner"></div>
    <div class="photo-dog" role="img" aria-label="Photo of a happy black pit bull type dog sitting beside the banner"></div>

    <p class="intro">The WNW Mobile Pet Care Team will be on-site to provide FREE:</p>

    <ul class="services services-left">
      <li>Veterinary Wellness Checks</li>
      <li>Vaccinations</li>
      <li>Microchipping</li>
      <li>Spay/Neuter Vouchers</li>
      <li>Dog Training &amp; Management Help</li>
    </ul>
    <ul class="services services-right">
      <li>Leashes, Collars &amp; Harnesses</li>
      <li>Jackets During the Winter Months</li>
      <li>Dog &amp; Cat Food</li>
      <li>Answers to Husbandry Questions</li>
      <li>Toys!!!</li>
    </ul>

    <h2 class="join">PLEASE JOIN US!</h2>
    <div class="date-box" aria-label="Space for clinic date"></div>
  </main>
</body>
</html>
```